We need a Word Template for Custom Laboratory Results from an independent laboratory

The test is a novel biomarker for a chronic pain condition called endometriosis. It is expressed as a percentage. We will upload a sample result. We are looking for improved graphic fidelity with more attention to design and spacing. Emphasis should be placed on the overall result, i.e. the patient percentage results. Considerationis going to be given to the most appealing graphic result.

Target Market(s)

Women aged 19-45

Colors
0054AA
0677BA
7BADD7
CADEEF
E8F1F8

```html
<!DOCTYPE html>
<html lang="en">
<head>
<meta charset="UTF-8">
<title>Endovia Micro-RNA Endometriosis Assay – Results</title>
<link rel="stylesheet" href="https://fonts.googleapis.com/css2?family=Montserrat:wght@400;500;600;700&display=swap">
<style>
  :root {
    --blue-deep: #0054AA;
    --blue-main: #0677BA;
    --blue-title: #0A6FAA;
    --blue-result: #0B5F93;
    --blue-soft: #7BADD7;
    --blue-pale: #CADEEF;
    --blue-wash: #E8F1F8;
    --ink: #3E3E3E;
    --ref-bg: #E4E4E4;
    --paper: #FFFFFF;
    --logo-teal: #6FA8B3;
    --logo-ink: #4A4F55;
  }
  * { box-sizing: border-box; margin: 0; padding: 0; }
  html, body { width: 960px; height: 1200px; overflow: hidden; }
  body {
    background: var(--paper);
    font-family: "Montserrat", Arial, sans-serif;
    position: relative;
  }
  .brand-row {
    position: absolute; left: 46px; top: 110px;
    display: flex; align-items: center; gap: 44px;
  }
  .brand { display: flex; align-items: center; gap: 10px; }
  .brand-mark {
    width: 44px; height: 44px; border-radius: 50%;
    background: var(--logo-teal);
  }
  .brand-clinic { font-size: 22px; font-weight: 500; color: var(--logo-ink); }
  .brand-lab { font-size: 30px; font-weight: 600; color: var(--blue-deep); }

  .report-title {
    position: absolute; left: 46px; top: 248px;
    font-size: 50px; font-weight: 700; line-height: 56px;
    letter-spacing: 1.5px; color: var(--blue-title);
  }
  .section-band {
    position: absolute; left: 46px; top: 379px; width: 872px; height: 50px;
    background: var(--blue-main);
    color: #fff; font-size: 20px; font-weight: 700; letter-spacing: 0.5px;
    display: flex; align-items: center; padding-left: 36px;
  }
  .patient { position: absolute; left: 81px; top: 472px; }
  .patient-line {
    font-size: 15px; font-weight: 700; color: var(--ink);
    height: 38px; display: flex; gap: 34px;
  }
  .result-box {
    position: absolute; top: 610px; height: 133px;
    background: linear-gradient(to bottom, var(--blue-wash), var(--blue-pale));
  }
  .result-label {
    left: 47px; width: 479px;
    display: flex; flex-direction: column; justify-content: center; align-items: center;
    text-align: center; color: var(--blue-main); font-size: 18px; line-height: 30px;
  }
  .result-label strong { font-weight: 700; }
  .result-value {
    left: 539px; width: 379px;
    display: flex; align-items: center; justify-content: center;
    font-size: 72px; font-weight: 700; color: var(--blue-result);
  }
  .reference {
    position: absolute; left: 47px; top: 834px; width: 871px; height: 236px;
    background: var(--ref-bg); padding: 34px 34px;
  }
  .reference h2 {
    font-size: 21px; font-weight: 600; color: var(--blue-main);
    letter-spacing: 0.5px; margin-bottom: 14px;
  }
  .reference ol { list-style: none; }
  .reference li {
    font-size: 18px; color: var(--blue-main); line-height: 30px;
  }
  .reference .num { display: inline-block; width: 30px; padding-left: 4px; }
</style>
</head>
<body>
  <header class="brand-row">
    <div class="brand">
      <span class="brand-mark"></span>
      <span class="brand-clinic">Meridian Fertility</span>
    </div>
    <span class="brand-lab">Lumora Labs</span>
  </header>

  <h1 class="report-title">ENDOVIA MICRO-RNA<br>ENDOMETRIOSIS ASSAY</h1>

  <div class="section-band">YOUR RESULTS</div>

  <section class="patient">
    <div class="patient-line"><span>[FIRST NAME]</span><span>[LAST NAME]</span></div>
    <div class="patient-line"><span>[OHIP NUMBER (12 CHARACTERS)]</span></div>
    <div class="patient-line"><span>[DOB]</span></div>
  </section>

  <div class="result-box result-label">
    <strong>Predicted probability of endometreosis</strong>
    <span>Compared to</span>
    <strong>Surgical Controls (100% Probability)</strong>
  </div>
  <div class="result-box result-value">38.7%</div>

  <section class="reference">
    <h2>REFERENCE RANGE</h2>
    <ol>
      <li><span class="num">1.</span> 0.0 - 29.9% - low probability of endometriosis</li>
      <li><span class="num">2.</span>29.9 - 44.9% - inconclusive</li>
      <li><span class="num">3.</span>45.0 - 55.0% - intermediate risk of endometriosis</li>
      <li><span class="num">4.</span> 55.1 - 64.9% - probable endometriosis</li>
      <li><span class="num">5.</span>65.0 - 99.9% - highly probable endometriosis</li>
    </ol>
  </section>
</body>
</html>
```